Real Estate Managemene Company Needs Business Card Design

We have a logo design and just need business cards made now for our business. Please use PDF logo # 3.

Card with Information to be attached shortly.

The card is used for a real estate management company. We will need to add four other employees and their cards.

Industry/Entity Type

Real Estate

Contact Information for Business Card

Tariq Hamdan
President
3187 Thornwick Avenue
Suite C
Glendale Heights, IL 60152
Phone 630.417.2286
Fax 630.417.2287
Cell 630.473.8062
vantorp@mailbreeze.net

Once design is approved we will have four other employees
Omar Hamdan
Operations Manager

Nadia Hamdan
Administrative Manager

Faz Hamdan
Principal

We would need to take out the cell # 630.473.8062 out for the remaining three cards.

Requirements
Must have
• Please use logo attached

```html
<!DOCTYPE html>
<html lang="en">
<head>
<meta charset="utf-8">
<title>Crestline Property Management Group – Business Card</title>
<link rel="stylesheet" href="https://fonts.googleapis.com/css2?family=Cinzel:wght@700&family=Lora:wght@400&display=swap">
<style>
  :root {
    --backdrop: #a8a6a7;
    --card: #f3f3f2;
    --brand-blue: #2d5a8a;
    --ink: #2b2b2b;
    --swoosh: #2a2a2a;
    --text: #3a3a3a;
    --on-blue: #ffffff;
  }
  * { margin: 0; padding: 0; box-sizing: border-box; }
  html, body {
    width: 1200px; height: 1200px; overflow: hidden;
    background: var(--backdrop);
  }
  .canvas { position: relative; width: 1200px; height: 1200px; }
  .card {
    position: absolute; width: 716px; height: 418px;
    background: var(--card); overflow: hidden;
  }
  .card--front { left: 240px; top: 118px; }
  .card--back { left: 232px; top: 643px; }

  .brand {
    position: absolute; display: flex; flex-direction: column; align-items: center;
    font-family: "Lora", serif; font-weight: 400; color: var(--ink); text-align: center;
  }
  .brand__mark { background: var(--brand-blue); }
  .brand__name { display: block; line-height: 1.1; }
  .brand__tagline { display: block; line-height: 1.2; }

  .card--front .brand { left: 0; right: 0; top: 112px; }
  .card--front .brand__mark { width: 96px; height: 96px; margin-bottom: 22px; }
  .card--front .brand__name { font-size: 58px; }
  .card--front .brand__tagline { font-size: 20px; margin-top: 4px; }

  .card--back .brand { left: 38px; width: 330px; top: 108px; }
  .card--back .brand__mark { width: 72px; height: 72px; margin-bottom: 16px; }
  .card--back .brand__name { font-size: 42px; }
  .card--back .brand__tagline { font-size: 14px; margin-top: 3px; }

  .header-shape { position: absolute; left: 0; top: 0; }

  .holder {
    position: absolute; right: 52px; top: 38px; text-align: right; color: var(--on-blue);
  }
  .holder__name { font-family: "Cinzel", serif; font-weight: 700; font-size: 25px; letter-spacing: 0.5px; }
  .holder__title { font-family: "Lora", serif; font-size: 16px; margin-top: 4px; }

  .address {
    position: absolute; left: 37px; top: 334px; font-style: normal;
    font-family: "Lora", serif; font-size: 17px; line-height: 25px; color: var(--text);
  }
  .contacts {
    position: absolute; right: 52px; top: 292px; list-style: none;
    font-family: "Lora", serif; font-size: 16px; line-height: 23px; color: var(--text);
  }
  .contacts li { display: flex; justify-content: flex-end; align-items: center; gap: 10px; }
  .contacts svg { width: 16px; height: 14px; fill: var(--brand-blue); flex: none; }
</style>
</head>
<body>
<div class="canvas">

  <section class="card card--front">
    <div class="brand">
      <span class="brand__mark"></span>
      <span class="brand__name">Crestline</span>
      <span class="brand__tagline">Property Management Group</span>
    </div>
  </section>

  <section class="card card--back">
    <svg class="header-shape" width="716" height="418" viewBox="0 0 716 418">
      <path fill="var(--brand-blue)" d="M0,0 H716 V168 C600,165 500,120 400,85 C280,42 140,30 0,40 Z"/>
      <path fill="var(--swoosh)" d="M0,44 C140,30 280,46 400,88 C500,123 600,166 716,170 V186 C600,182 500,140 400,106 C280,64 140,48 0,62 Z"/>
    </svg>

    <div class="holder">
      <div class="holder__name">Tariq Hamdan</div>
      <div class="holder__title">President</div>
    </div>

    <div class="brand">
      <span class="brand__mark"></span>
      <span class="brand__name">Crestline</span>
      <span class="brand__tagline">Property Management Group</span>
    </div>

    <address class="address">
      3187 Thornwick Avenue<br>
      Suite C Glendale Heights, IL 60152
    </address>

    <ul class="contacts">
      <li>630.473.8062
        <svg viewBox="0 0 16 14" aria-label="Cell"><rect x="4" y="0" width="8" height="14" rx="1.5"/><rect x="5.5" y="2" width="5" height="8" fill="var(--card)"/></svg>
      </li>
      <li>630.417.2286
        <svg viewBox="0 0 16 14" aria-label="Phone"><path d="M1,4 C1,1 15,1 15,4 V6 H11 V4 H5 V6 H1 Z"/><path d="M3,7 H13 L15,13 H1 Z"/></svg>
      </li>
      <li>630.417.2287
        <svg viewBox="0 0 16 14" aria-label="Fax"><rect x="4" y="0" width="8" height="4"/><rect x="0" y="4" width="16" height="7" rx="1"/><rect x="4" y="9" width="8" height="5" fill="var(--brand-blue)" stroke="var(--card)" stroke-width="1"/></svg>
      </li>
      <li>vantorp@mailbreeze.net
        <svg viewBox="0 0 16 14" aria-label="Email"><rect x="0" y="2" width="16" height="11"/><path d="M0,2 L8,9 L16,2" fill="none" stroke="var(--card)" stroke-width="1.3"/></svg>
      </li>
    </ul>
  </section>

</div>
</body>
</html>
```